Mini Leporello with Tartar Recipe from Christmas Apéro

As present from our christmas apero we would like to give our visitors a little booklet of the tartar recipes they enjoyed with us. For this we need a little pocket recipe booklet. ISt should be a Mini-Leparello. You can find the content attached.

Target Market(s)

customers christmas apero

Font styles to use
Other font styles liked:
• FS albert

Requirements
Must have
• each recipe comes from Velmar or Markus Tobler - it should show the author
• the format should be 85 x 85 mm and I need a printable file

```html
<!DOCTYPE html>
<html lang="de">
<head>
<meta charset="utf-8">
<title>Tartar-Rezepte vom Laterne – Leporello</title>
<link href="https://fonts.googleapis.com/css2?family=Encode+Sans+Condensed:wght@500;600&family=Mulish:wght@400;500&display=swap" rel="stylesheet">
<style>
  :root {
    --red: #e1141f;
    --paper: #f5f5f5;
    --ink: #2b2b2b;
    --rule: #6f6f6f;
    --stage: #dcdcdc;
  }
  * { box-sizing: border-box; margin: 0; padding: 0; }
  html, body { width: 1200px; height: 900px; overflow: hidden; }
  body {
    background: var(--stage);
    font-family: "Mulish", sans-serif;
    color: var(--ink);
  }
  .leporello {
    position: absolute;
    left: 30px; top: 307px;
    display: flex;
  }
  .panel {
    width: 285px; height: 285px;
    background: var(--paper);
    border-top: 4px solid var(--red);
    border-bottom: 4px solid var(--red);
    border-left: 2px solid var(--red);
    position: relative;
    padding: 12px 12px 0;
    overflow: hidden;
  }
  .panel:first-child { border-left-width: 4px; }
  .panel:last-child { border-right: 4px solid var(--red); }

  /* cover */
  .cover { display: flex; flex-direction: column; align-items: center; padding-top: 30px; }
  .title-block { width: 100%; position: relative; padding: 10px 0 8px; text-align: center; }
  .title-rule { position: absolute; left: 4px; right: 4px; height: 1px; background: var(--rule); }
  .title-rule.top { top: 0; }
  .title-rule.bottom { bottom: 0; }
  .title-rule::after {
    content: ""; position: absolute; left: 50%; top: -3px; width: 7px; height: 7px;
    margin-left: -3.5px; border: 1px solid var(--rule); border-radius: 50%; background: var(--paper);
  }
  .cover-title {
    font-family: "Encode Sans Condensed", sans-serif; font-weight: 500;
    color: var(--red); font-size: 29px; line-height: 1; text-transform: uppercase;
  }
  .cover-subtitle {
    color: var(--red);
    font-size: 10px; letter-spacing: 4px; margin-top: 5px;
  }
  .brand { display: flex; align-items: center; gap: 8px; margin-top: 30px; }
  .brand-square { width: 14px; height: 14px; background: var(--red); }
  .brand-name {
    font-family: "Encode Sans Condensed", sans-serif; font-weight: 600;
    color: var(--red); font-size: 30px;
  }
  .cover-credit { position: absolute; bottom: 10px; left: 0; right: 0; text-align: center; font-size: 8px; }

  /* recipe */
  .recipe-photo { height: 136px; }
  .recipe-body {
    display: flex; border-top: 1px solid var(--rule); margin-top: 8px; height: 117px;
  }
  .recipe-intro { width: 46%; flex: none; padding: 8px 6px 0 0; border-right: 1px solid var(--rule); }
  .recipe-name {
    font-family: "Encode Sans Condensed", sans-serif; font-weight: 600;
    color: var(--red); font-size: 16px; line-height: 1.05; margin-bottom: 10px;
  }
  .recipe-text { font-size: 6.3px; line-height: 1.4; }
  .ingredients {
    flex: 1; display: grid; grid-template-columns: auto auto; align-content: start;
    column-gap: 6px; padding: 8px 0 0 7px; font-size: 8.5px; line-height: 1.35;
  }
  .ingredients ul { list-style: none; }
  .ingredients li { position: relative; padding-left: 7px; white-space: nowrap; }
  .ingredients li::before { content: "•"; position: absolute; left: 0; top: 0; }
  .ingredients .wide { grid-column: 1 / -1; }
  .ingredients .note li { white-space: normal; }

  .tomato .recipe-name { margin-bottom: 4px; }
  .tomato .recipe-text { font-size: 5.6px; line-height: 1.35; }
  .tomato .ingredients { grid-template-columns: auto 1fr; }
</style>
</head>
<body>
<main class="leporello">
  <section class="panel cover">
    <div class="title-block">
      <span class="title-rule top"></span>
      <h1 class="cover-title">Tartar-Rezepte<br>vom Laterne</h1>
      <p class="cover-subtitle">WEIHNACHTSAPÉRO 2016</p>
      <span class="title-rule bottom"></span>
    </div>
    <div class="brand">
      <span class="brand-square"></span>
      <span class="brand-name">Velmar</span>
    </div>
    <p class="cover-credit">each recipe comes from Velmar or Markus Tobler</p>
  </section>

  <section class="panel recipe">
    <div class="recipe-photo" role="img" aria-label="Rindertartar auf weissem Teller mit Salat und Brot" style="background: linear-gradient(120deg,#3f5a2c 0%,#b8324a 45%,#e7dcd3 80%,#d79a55 100%);"></div>
    <div class="recipe-body">
      <div class="recipe-intro">
        <h2 class="recipe-name">Rindertartar</h2>
        <p class="recipe-text">Alle Zutaten fein hacken und mischen:</p>
      </div>
      <div class="ingredients">
        <ul><li>Rindsfilet</li><li>Essiggurken</li><li>Oliven</li><li>Peperoni</li><li>Kapern</li></ul>
        <ul><li>Zwiebel</li><li>Essig</li><li>Senf</li><li>Pfeffer</li><li>Salz</li></ul>
      </div>
    </div>
  </section>

  <section class="panel recipe">
    <div class="recipe-photo" role="img" aria-label="Ligurisches Kalbstartar mit Parmesansplitter auf grüner Sauce" style="background: linear-gradient(135deg,#6a6048 0%,#7a4a3c 40%,#4f9a3a 70%,#d9d8d2 100%);"></div>
    <div class="recipe-body">
      <div class="recipe-intro">
        <h2 class="recipe-name">Ligurisches Kalbstartar</h2>
        <p class="recipe-text">Alle Zutaten fein hacken und mischen:</p>
      </div>
      <div class="ingredients">
        <ul><li>Kalbfleisch</li><li>Zitronen</li><li>Olivenoel</li></ul>
        <ul><li>Knoblauch</li><li>Pfeffer</li><li>Salz</li></ul>
        <ul class="wide"><li>Grosszügig Parmesansplitter</li></ul>
      </div>
    </div>
  </section>

  <section class="panel recipe tomato">
    <div class="recipe-photo" role="img" aria-label="Tomatentartar mit Kräutern auf rosa Glasteller" style="background: linear-gradient(130deg,#f1e6ea 0%,#c7363a 50%,#a9c07a 70%,#efe3e6 100%);"></div>
    <div class="recipe-body">
      <div class="recipe-intro">
        <h2 class="recipe-name">Tomatentartar</h2>
        <p class="recipe-text">Im Prinzip ist das Tomatentartar ein klassisches Rindstartar, anstelle des Fleisches nimmt man getrocknete, in Oel eingelegte Tomaten. Giessen Sie den Grossteil des Oels ab, tupfen Sie die Tomaten nicht trocken. Zerkleinern Sie die Tomaten mit dem Pürierstab (nicht zu fein) und geben folgende Zutaten hinzu:</p>
      </div>
      <div class="ingredients">
        <ul><li>Eigelb</li><li>Kapern</li><li>Basilikum</li><li>Cognac</li><li>Pfeffer</li><li>Salz</li></ul>
        <ul class="note"><li>Weitere Gewürze nach Abschmecken, bzw. je nach Würzigkeit der im Oel eingelegten Tomaten</li></ul>
      </div>
    </div>
  </section>
</main>
</body>
</html>
```